7 3/4 x 5 1/4 Annual Banquet Invitation

Design an invitation for our Chamber's annual banquet. It will be a single sided invitation 5 1/4" wide by 7 3/4" height that we will print in-house. Our logo is attached. The theme is "Serving Together". I was thinking of an image with two hands coming together in a handshake, perhaps intertwining our logo colors. This is just a thought. I am open for any suggestions! Text for the invitation should be as follows: The Board of Directors and Staff cordially invites you to attend the 64th Yearly Gathering & Micro-Trade Fair - Monday, January 22, 2018. 5:30 p.m. Social, 6:00 p.m. Dinner. Cedarvale Chapel, 4819 Harlan P. Moss Rd S, Ashbury. Please RSVP by January 18, 2018.

Target Market(s)

This invitation will be printed and mailed to our membership.

Industry/Entity Type

Business Management

Colors
33a6d7
faa54b
0355a3
00a990

Requirements
Must have
• Event info as indentified above.
Nice to have
• Our Logo

```html
<!DOCTYPE html>
<html lang="en">
<head>
<meta charset="utf-8">
<title>Serving Together – Annual Banquet Invitation</title>
<link href="https://fonts.googleapis.com/css2?family=Cinzel:wght@400;500;600&family=Montserrat:wght@900&display=swap" rel="stylesheet">
<style>
  :root {
    --page: #ffffff;
    --photo-dark: #1f2a30;
    --photo-mid: #55606a;
    --photo-light: #b9b3ad;
    --orange: #f7941d;
    --orange-edge: #d9822a;
    --navy: #0e2a82;
    --ink: #1a1a1a;
    --panel: rgba(222, 226, 230, 0.62);
    --gold: rgba(250, 211, 72, 0.88);
    --rule: #3a3a3a;
  }
  html, body {
    margin: 0;
    width: 1200px;
    height: 1192px;
    overflow: hidden;
    background: var(--page);
  }
  .invitation {
    position: absolute;
    left: 204px;
    top: 11px;
    width: 792px;
    height: 1170px;
    overflow: hidden;
  }
  .hero-photo {
    position: absolute;
    inset: 0;
    background:
      radial-gradient(ellipse 55% 40% at 52% 55%, var(--photo-light) 0%, rgba(185,179,173,0) 70%),
      linear-gradient(180deg, var(--photo-dark) 0%, var(--photo-mid) 45%, #6c6660 62%, var(--photo-dark) 100%);
  }
  .theme-title {
    position: absolute;
    left: 0;
    width: 100%;
    margin: 0;
    font-family: "Montserrat", sans-serif;
    font-weight: 900;
    color: var(--orange);
    letter-spacing: -4px;
    line-height: 1;
    text-shadow: 4px 6px 6px rgba(0,0,0,0.55);
  }
  .theme-title span {
    position: absolute;
    display: block;
    white-space: nowrap;
  }
  .theme-serving { left: 174px; top: 146px; font-size: 100px; }
  .theme-together { left: 141px; top: 224px; font-size: 100px; }
  .details-panel {
    position: absolute;
    left: 126px;
    top: 310px;
    width: 553px;
    height: 699px;
    background: var(--panel);
    border: 2px solid var(--orange-edge);
    text-align: center;
    font-family: "Cinzel", serif;
    color: var(--ink);
  }
  .invite-line {
    position: absolute;
    left: 0;
    right: 0;
    top: 52px;
    margin: 0;
    font-size: 17px;
    line-height: 24px;
    letter-spacing: 1px;
  }
  .event-name {
    position: absolute;
    left: 0;
    right: 0;
    top: 122px;
    margin: 0;
    font-family: "Cinzel", serif;
    font-weight: 500;
    font-size: 50px;
    line-height: 45px;
    letter-spacing: -3px;
    color: var(--navy);
  }
  .event-date {
    position: absolute;
    left: 0;
    right: 0;
    top: 323px;
    margin: 0;
    font-size: 24px;
    font-weight: 500;
    letter-spacing: 1px;
  }
  .schedule-box {
    position: absolute;
    left: 47px;
    top: 368px;
    width: 458px;
    height: 128px;
    border-radius: 18px;
    background: var(--gold);
    font-size: 17px;
    font-weight: 500;
    letter-spacing: 0.5px;
  }
  .schedule-box p { margin: 0; line-height: 24px; }
  .schedule-box .time { padding-top: 8px; }
  .schedule-box .rule {
    width: 390px;
    height: 1px;
    margin: 3px auto 3px;
    background: var(--rule);
  }
  .organiser {
    position: absolute;
    left: 0;
    right: 0;
    top: 624px;
    margin: 0;
    font-family: "Cinzel", serif;
    font-weight: 600;
    font-size: 20px;
    line-height: 22px;
    color: var(--navy);
    letter-spacing: 0.5px;
  }
  .organiser small {
    display: block;
    font-size: 13px;
    letter-spacing: 3px;
  }
</style>
</head>
<body>
  <main class="invitation">
    <div class="hero-photo" role="img" aria-label="Photograph of many hands stacked together in a circle, seen from above, softly blurred"></div>

    <h1 class="theme-title">
      <span class="theme-serving">SERVING</span>
      <span class="theme-together">TOGETHER</span>
    </h1>

    <section class="details-panel">
      <p class="invite-line">The Board of Directors and<br>Staff cordially invites you to attend</p>
      <h2 class="event-name">The 64th<br>Yearly Gathering<br>&amp; Micro-Trade<br>Fair.</h2>
      <p class="event-date">Monday, January 22, 2018.</p>
      <div class="schedule-box">
        <p class="time">5:30 p.m. Social, 6:00 p.m.</p>
        <div class="rule"></div>
        <p>Dinner - Cedarvale Chapel,<br>4819 Harlan P. Moss Rd S, Ashbury.</p>
        <div class="rule"></div>
        <p>Please RSVP by January 18, 2018.</p>
      </div>
      <p class="organiser">Brookfield Chamber<small>of Commerce &amp; Tourism</small></p>
    </section>
  </main>
</body>
</html>
```